NEW Modern Sleek Business Card for VR Language Startup

Our startup is using VR to lead the next wave of world language education. We need a two-sided business card that introduces the larger organization (Quorvel Language Inc) and our contact info on one side and shows the product, Lumidrasca, on the other side.

Side 1 (contact info)= Quorvel Logo and Contact info (name, title, phone, email)

Side 2 (product)= Lumidrasc logo, text, and website
Text= Culturally Immersive Language Learning Games
Website= www.lumidrasc.example

Target Market(s)

Education, Technology

Contact Information for Business Card

Contact info will be updated upon approval of the design. For now, put this as a placeholder.

Perry Hollins
Founder & CEO
phollins@mailtrove.example
(555)-014-2736

Font styles to use
Other font styles liked:
• Gibson and Century Gothic are the brand fonts

Requirements
Nice to have
• I would love to see cohesion between the design and colors of the two logos. I have attached a few business card designs that I like, so you can get a feel for my preferred style.

```html
<!DOCTYPE html>
<html lang="en">
<head>
<meta charset="utf-8">
<title>Quorvel Language – Business Card</title>
<link rel="stylesheet" href="https://fonts.googleapis.com/css2?family=Montserrat:wght@600;700&family=Questrial&display=swap">
<style>
  :root {
    --page-bg: #e4e4e6;
    --card-bg: #ffffff;
    --ink: #1d1d1f;
    --ink-soft: #3b3b3d;
    --accent-red: #f0333f;
    --accent-violet: #5b4ff5;
    --grad-orange: #f4a737;
    --grad-red: #fb3440;
    --grad-purple: #635bf5;
    --grad-cyan: #22d3ee;
  }
  * { box-sizing: border-box; margin: 0; padding: 0; }
  html, body { width: 1200px; height: 1200px; overflow: hidden; }
  body {
    background: var(--page-bg);
    font-family: "Questrial", "Century Gothic", sans-serif;
    color: var(--ink);
    position: relative;
  }
  .card {
    position: absolute;
    left: 150px;
    width: 900px;
    height: 514px;
    background: var(--card-bg);
    border-radius: 30px;
    overflow: hidden;
    box-shadow: 0 10px 30px rgba(0,0,0,0.18);
  }
  /* Product side */
  .card--product { top: 64px; }
  .product-brand {
    position: absolute;
    top: 130px; left: 0; right: 0;
    display: flex; flex-direction: column; align-items: center;
  }
  .product-brand__mark {
    width: 120px; height: 120px; border-radius: 50%;
    background: linear-gradient(160deg, var(--grad-cyan), var(--grad-purple));
    margin-bottom: 24px;
  }
  .product-brand__name {
    font-size: 62px;
    color: var(--ink-soft);
    letter-spacing: 1px;
    line-height: 1;
  }
  .product-tagline {
    margin-top: 14px;
    font-size: 22px;
    color: var(--ink-soft);
    letter-spacing: 0.5px;
  }
  .product-url {
    position: absolute;
    bottom: 58px; left: 0; right: 0;
    text-align: center;
    font-family: "Montserrat", sans-serif;
    font-weight: 700;
    font-size: 22px;
    color: var(--accent-violet);
    letter-spacing: 0.5px;
  }
  /* Contact side */
  .card--contact { top: 622px; }
  .company-brand {
    position: absolute; top: 70px; left: 70px;
    display: flex; align-items: center; gap: 18px;
  }
  .company-brand__mark {
    width: 64px; height: 64px; border-radius: 50%;
    background: linear-gradient(200deg, var(--grad-orange), var(--grad-red) 40%, var(--grad-purple) 75%, var(--grad-cyan));
  }
  .company-brand__name {
    font-size: 30px;
    color: var(--ink);
    letter-spacing: 6px;
    line-height: 1.15;
  }
  .contact-person { position: absolute; top: 230px; left: 70px; }
  .contact-person__name {
    font-family: "Montserrat", sans-serif;
    font-weight: 700;
    font-size: 34px;
    letter-spacing: 0.5px;
  }
  .contact-person__title { font-size: 20px; color: var(--ink-soft); margin-top: 2px; }
  .contact-person__rule { width: 44px; height: 2px; background: var(--accent-red); margin-top: 12px; }
  .contact-list { position: absolute; top: 360px; left: 70px; list-style: none; }
  .contact-list__item {
    display: flex; align-items: center; gap: 14px;
    font-size: 20px; margin-bottom: 14px;
  }
  .contact-list__icon { width: 20px; height: 20px; flex: none; }
  .feature-orb {
    position: absolute;
    width: 560px; height: 560px; border-radius: 50%;
    right: -60px; top: 40px;
    background: linear-gradient(210deg, var(--grad-orange) 5%, var(--grad-red) 35%, var(--grad-purple) 70%, var(--grad-cyan) 95%);
  }
</style>
</head>
<body>

<section class="card card--product" aria-label="Product side">
  <div class="product-brand">
    <div class="product-brand__mark"></div>
    <div class="product-brand__name">Lumidrasc</div>
    <p class="product-tagline">Culturally Immersive Language Learning Games</p>
  </div>
  <p class="product-url">www.lumidrasc.example</p>
</section>

<section class="card card--contact" aria-label="Contact side">
  <div class="feature-orb" role="img" aria-label="Large gradient brand decoration"></div>

  <div class="company-brand">
    <div class="company-brand__mark"></div>
    <div class="company-brand__name">QUORVEL<br>LANGUAGE</div>
  </div>

  <div class="contact-person">
    <h1 class="contact-person__name">PERRY HOLLINS</h1>
    <p class="contact-person__title">President</p>
    <div class="contact-person__rule"></div>
  </div>

  <ul class="contact-list">
    <li class="contact-list__item">
      <svg class="contact-list__icon" viewBox="0 0 20 20" aria-hidden="true">
        <rect x="1" y="4" width="18" height="13" rx="1.5" fill="none" stroke="#f0333f" stroke-width="2"/>
        <path d="M1.5 5 L10 11.5 L18.5 5" fill="none" stroke="#f0333f" stroke-width="2"/>
      </svg>
      <span>phollins@mailtrove.example</span>
    </li>
    <li class="contact-list__item">
      <svg class="contact-list__icon" viewBox="0 0 20 20" aria-hidden="true">
        <circle cx="10" cy="10" r="8.5" fill="none" stroke="#f0333f" stroke-width="1.8"/>
        <ellipse cx="10" cy="10" rx="3.8" ry="8.5" fill="none" stroke="#f0333f" stroke-width="1.5"/>
        <path d="M1.5 10 H18.5 M3 5.5 H17 M3 14.5 H17" stroke="#f0333f" stroke-width="1.5"/>
      </svg>
      <span>(555)-014-2736</span>
    </li>
  </ul>
</section>

</body>
</html>
```